Letterhead design - Harwick Group

We have just had our Logo created and our now wantng a letterhead design to incorporate this. Please use the same colours as in the logo, which is attached.
Please use the company details below
P O Box 86, Bleneheim 7315
Ph: 03 642 1937
dave@harwickgroup.co.nz
We would like a professional look
We need an overall letterhead design for our varied group of buisinesses which are based in NZ and overseas. We grow and develop buisinesses. Our companies began in NZ but we now have branches overseas as well. People are our greatest asset and we employ some incredible staff. Our buisinesses are scientific, innovative and growing in size and expertise with a financial base.

Target Market(s)

Professionals

Industry/Entity Type

Investment

Requirements
Must have
• Easy to read.
• Please use the same colours as in the logo
• Please use the company details below
• P O Box 86, Bleneheim 7315
• Ph: 03 642 1937
• dave@harwickgroup.co.nz

```html
<!DOCTYPE html>
<html lang="en">
<head>
<meta charset="utf-8">
<title>Harwick Group Letterhead</title>
<link rel="stylesheet" href="https://fonts.googleapis.com/css2?family=Lato:wght@400;700&family=Roboto:wght@400&display=swap">
<style>
:root{
  --backdrop:#cbcbcb;
  --paper:#ffffff;
  --brand-green:#1fb56f;
  --ink:#4a4a4a;
  --ink-dark:#333333;
  --icon:#555555;
  --signature:#3a3a3a;
}
*{margin:0;padding:0;box-sizing:border-box}
html,body{width:1200px;height:1200px;overflow:hidden;background:var(--backdrop)}
.letterhead{
  position:absolute;left:191px;top:20px;width:818px;height:1160px;
  background:var(--paper);box-shadow:0 2px 6px rgba(0,0,0,.18);
  font-family:"Lato",sans-serif;color:var(--ink);overflow:hidden;
}
.brand{position:absolute;left:54px;top:74px;display:flex;align-items:center;gap:10px}
.brand-square{width:34px;height:34px;background:var(--brand-green)}
.brand-name{font-family:"Lato",sans-serif;font-weight:700;font-size:30px;color:var(--brand-green);letter-spacing:1px;text-transform:uppercase}
.contact{position:absolute;right:55px;top:51px;font-family:"Roboto",sans-serif;font-size:13.5px;color:var(--ink-dark);list-style:none}
.contact li{display:flex;align-items:center;justify-content:flex-end;gap:9px;height:23.5px}
.contact svg{width:14px;height:14px;flex:none}
.header-rule{position:absolute;left:0;top:181px;width:818px;height:14px}
.letter-body{position:absolute;left:55px;top:317px;width:710px}
.sender-name{font-size:13px;color:var(--ink-dark);line-height:16px}
.sender-role{font-size:10.5px;color:var(--ink-dark);line-height:13px}
.letter-date{margin-top:23px;font-size:11px;color:var(--ink-dark)}
.letter-date sup{font-size:6px}
.salutation{margin-top:14px;font-size:12.5px;color:var(--ink-dark)}
.para{font-size:11.6px;line-height:19.3px;text-align:justify;text-align-last:left}
.p1{position:absolute;top:133px}
.p2{position:absolute;top:229px}
.p3{position:absolute;top:344px}
.p4{position:absolute;top:440px}
.closing{position:absolute;top:597px;font-size:13px;color:var(--ink-dark)}
.signature{position:absolute;left:55px;top:925px;width:145px;height:24px;background:linear-gradient(90deg,rgba(58,58,58,.18),rgba(58,58,58,.06))}
.footer-band{position:absolute;left:0;bottom:0;width:818px;height:27px;background:var(--brand-green)}
</style>
</head>
<body>
<main class="letterhead">
  <header>
    <div class="brand">
      <span class="brand-square"></span>
      <span class="brand-name">Harwick Group</span>
    </div>
    <ul class="contact">
      <li>03 642 1937
        <svg viewBox="0 0 16 16"><path d="M4 1.5l2.5 3-1.5 1.6c.8 1.9 2.3 3.4 4.2 4.2l1.6-1.5 3 2.5-1.6 2.2C7 13.2 2.8 9 1.9 3.1z" fill="none" stroke="var(--icon)" stroke-width="1.4" stroke-linejoin="round"/></svg>
      </li>
      <li>P O Box 86, Bleneheim 7315
        <svg viewBox="0 0 16 16"><rect x="1" y="3.5" width="14" height="9" fill="var(--icon)"/><path d="M1 3.5l7 5 7-5" fill="none" stroke="#fff" stroke-width="1"/></svg>
      </li>
      <li>dave@harwickgroup.co.nz
        <svg viewBox="0 0 16 16" fill="none" stroke="var(--icon)" stroke-width="1.2"><circle cx="8" cy="8" r="6.5"/><ellipse cx="8" cy="8" rx="3" ry="6.5"/><path d="M1.5 8h13M2.5 4.8h11M2.5 11.2h11"/></svg>
      </li>
    </ul>
    <svg class="header-rule" viewBox="0 0 818 14" preserveAspectRatio="none" aria-hidden="true">
      <polygon points="0,0 269,0 283,10 818,10 818,14 0,14" fill="var(--brand-green)"/>
    </svg>
  </header>

  <section class="letter-body">
    <p class="sender-name">RENATA KOWALSKI</p>
    <p class="sender-role">Maneging Director</p>
    <p class="letter-date">11<sup>st</sup> February, 2018</p>
    <p class="salutation">Dear Mr. Hale,</p>

    <p class="para p1">Lorem ipsum dolor sit amet, consectetur adipisicing elit, sed do eiusmod tempor incididunt ut labore et dolore magna sdfsd sfdsf sd veniam, quis nostrud exercitation&nbsp; ullamco laboris nisi ut aliquip ex ea commodo consequat. Duis aute irure dolor in repsdfsdf sdfsd ullamco laboris nisi ut aliquip ex ea commodo consequat. Duis aute irure dolor in reprehenderit in voluptate velit esse cillum dolore eu fugiat nulla pariatur. Excepteur sint occaecat cupidat</p>
    <p class="para p2">Lorem ipsum dolor sit amet, consectetur adipisicing elit, sed do eiusmod tempor incididunt ut labore et dolore magna sdfsdfsdfdfdf veniam, quis nostrud exercitation&nbsp; ullamco laboris nisi ut aliquip ex ea commodo consequat. Duis aute irure dolor in repdfgfgr rtetg. ullamco laboris nisi ut aliquip ex ea commodo consequat. Duis aute irure dolor in reprehenderit in voluptate velit esse cillum dolore eu fugiat nulla pariatur. Excepteur sint occaecat cupidatat</p>
    <p class="para p3">Lorem ipsum dolor sit amet, consectetur adipisicing elit, sed do eiusmod tempor incididunt ut labore et dolore magna sds dff fefsdf veniam, quis nostrud exercitation&nbsp; ullamco laboris nisi ut aliquip ex ea commodo consequat. Duis aute irure dolor in repsdfsdf dfdsf ullamco laboris nisi ut aliquip ex ea commodo consequat. Duis aute irure dolor in reprehenderit in voluptate velit esse cillum dolore eu fugiat nulla pariatur. Excepteur sint occaecat cupidatat</p>
    <p class="para p4">dolor sit amet, consectetur, adipisci velit, sed quia non numquam eius modi tempora incidunt ut labore et</p>
    <p class="closing">Regards</p>
  </section>

  <div class="signature" role="img" aria-label="Handwritten signature of the managing director"></div>

  <footer class="footer-band"></footer>
</main>
</body>
</html>
```